Book Cover: The Quiet Lantern Keeper

DO NOT JUST COPY THE BOOK COVER I HAVE ADDED FOR REFERENCE. I NEED SOMETHING FRESH NOT JUST A COPY AND PASTE!
If you cannot improve on the design with something creative then don't submit a design.

Project Title:
Book Cover Design for The Quiet Lantern Keeper

Must be better than the mock design I have uploaded in project files.

Project Description:
I’m looking for a striking and emotionally evocative book cover for my upcoming title The Quiet Lantern Keeper. This is a deeply personal and powerful memoir about the masks we wear, emotional survival, control, and the journey toward radical self-awareness and healing. The cover should visually represent the contrast between the performative self and the authentic self.

Visual Concept:
Please take visual inspiration and design continuity from my previous book Rise Past Dusk! — I will upload that cover for reference. This new design should feel like a continuation of the same author journey, but bolder and more psychologically intense.

You’ll be provided with two photos of me:

One where I appear more unkept, raw, and emotionally heavy.

One where I appear clean, centered, and lighter.

These can either be:

Split down the middle to create a “mirror” or duality effect (symbolizing the split self),

Or placed side by side as a subtle before/after or internal/external representation.

You may also consider overlaying or fading one into the other if done tastefully.

The mood should hint at internal conflict, self-reckoning, and healing—but without looking too “self-help cliché.” Think masculine, introspective, modern, and editorial. Avoid overly bright or busy visuals. A minimal or clean design with strong type hierarchy is preferred.

Key Themes to Represent Visually (even abstractly):

Narcissism as a survival mechanism

The emotional cost of performance

The tension between image and authenticity

The healing journey from ego to empathy

Design References:

Rise Past Dusk! (uploaded) — continuity of brand and typography encouraged

Memoir-style covers like Every Harbor Has a Lighthouse, Driftwood, or A River Remembers Stones for layout feel

If using color, muted tones with contrast (black/white, sepia, desaturated blues or greys) work well

Title: The Quiet Lantern Keeper
Subtitle (optional placement): Not every narcissist is a monster. Some are just wounded men trying their best to survive
Author: Marek Tollan

Deliverables:

Full front cover for print sale size as previous cover, including space for subtitle and author name

Spine and back cover (leave placeholder text if no blurb is given)

Ebook cover version

High-resolution files suitable for Pellora PrintHub and print use

Additional Notes:
Please ensure the tone stays emotionally resonant, masculine, and sophisticated. No stock image models or cliché therapist symbols. Use my uploaded photos only.

Looking forward to seeing your vision come to life.

Back Cover Blurb – The Quiet Lantern Keeper
A brutally honest recovery story—about what happens after you get clean, and the ego you still have to face.
Most people think addiction ends when you put down the drink, the drug, or the chaos.
But for Marek Tollan, sobriety was just the start.
Behind the personal development posts, six-pack selfies, and billion-rand property deals, he was still chasing the one thing rehab never took from him: the need to be admired.
This book is not a confession. It’s a dismantling.
In The Quiet Lantern Keeper, Marek exposes the hidden patterns of ego, control, and validation-seeking that nearly cost him everything—even after he got “better.” With fearless self-inquiry and raw storytelling, he invites readers into his recovery from performance, perfectionism, and power addiction.
Whether you’ve been the narcissist—or you’ve loved one—this book is a mirror. And what you’ll find is not just insight, but a new path forward: one where truth is more powerful than charm, and safety matters more than being impressive.
This isn’t about being perfect.
It’s about being honest.
And finally becoming someone worth trusting—especially by yourself.

Target Market(s)

Any reader wanting to read about narcissism and love

Font styles to use
Sans Serif

Colors
EB3D1F
EC4F4E
F09395
F8D3D4
FCEDEE

Requirements
Must have
• Must be better than the mock design I uploaded.

```html
<!DOCTYPE html>
<html lang="en">
<head>
<meta charset="utf-8">
<title>The Quiet Lantern Keeper — Full Cover Wrap</title>
<link href="https://fonts.googleapis.com/css2?family=Oswald:wght@300;400;600;700&family=Rubik:wght@400&display=swap" rel="stylesheet">
<style>
  :root {
    --stage: #66605f;
    --charcoal: #1f1c1d;
    --charcoal-soft: #2a2627;
    --spine-ink: #151314;
    --sepia-half: #5c4a42;
    --sepia-deep: #3a2e2a;
    --slate-half: #4d5862;
    --slate-deep: #2e353c;
    --ember: #eb3d1f;
    --rose: #ec4f4e;
    --blush: #f09395;
    --pale-blush: #f8d3d4;
    --paper: #fcedee;
    --text-muted: #cfc6c4;
  }
  * { margin: 0; padding: 0; box-sizing: border-box; }
  html, body { width: 1200px; height: 1200px; overflow: hidden; }
  body { background: var(--stage); position: relative; font-family: 'Oswald', sans-serif; }

  .cover-wrap {
    position: absolute; left: 50px; top: 223px;
    width: 1100px; height: 754px;
    box-shadow: 0 10px 30px rgba(0,0,0,0.35);
    overflow: hidden; display: flex;
  }

  /* back cover */
  .back-cover {
    width: 515px; height: 754px; background: var(--charcoal-soft);
    padding: 64px 48px 0; text-align: center; color: var(--paper);
    border-top: 6px solid var(--ember);
  }
  .back-tagline {
    font-family: 'Oswald', sans-serif; font-weight: 400; font-size: 13px;
    letter-spacing: 1.5px; text-transform: uppercase; color: var(--blush);
    line-height: 19px;
  }
  .back-rule { width: 48px; height: 2px; background: var(--ember); margin: 18px auto; }
  .back-hook { font-weight: 600; font-size: 17px; line-height: 23px; color: var(--paper); }
  .back-blurb {
    margin-top: 16px; font-weight: 300; font-size: 14px; line-height: 21px;
    color: var(--text-muted);
  }
  .back-blurb p + p { margin-top: 8px; }
  .back-closing {
    margin-top: 18px; font-weight: 600; font-size: 16px; line-height: 24px;
    color: var(--pale-blush);
  }

  /* spine */
  .spine {
    width: 60px; height: 754px; background: var(--spine-ink);
    border-top: 6px solid var(--ember);
    display: flex; flex-direction: column; align-items: center;
    padding: 60px 0 50px; justify-content: space-between;
  }
  .spine-title, .spine-author {
    writing-mode: vertical-rl; font-size: 22px; letter-spacing: 2px; color: var(--paper);
  }
  .spine-title { font-weight: 300; }
  .spine-title b { font-weight: 700; }
  .spine-author { font-weight: 700; color: var(--blush); }

  /* front cover */
  .front-cover {
    position: relative; width: 525px; height: 754px; background: var(--charcoal);
    border-top: 6px solid var(--ember);
  }
  .portrait { position: absolute; right: 0; top: 0; width: 275px; height: 748px; }
  .endorsement {
    position: absolute; left: 36px; top: 30px; width: 450px;
    font-family: 'Rubik', sans-serif; font-size: 11px; line-height: 17px; color: var(--text-muted);
  }
  .endorsement .credit { font-family: 'Oswald', sans-serif; color: var(--blush); letter-spacing: 1px; }
  .title-block { position: absolute; left: 36px; top: 100px; color: var(--paper); }
  .title-lead { font-weight: 400; font-size: 26px; letter-spacing: 8px; color: var(--blush); line-height: 30px; }
  .title-main { font-weight: 700; font-size: 82px; line-height: 80px; text-transform: uppercase; }
  .title-rule { width: 64px; height: 4px; background: var(--ember); margin-top: 22px; }
  .subtitle {
    position: absolute; left: 36px; top: 470px; width: 230px;
    font-weight: 300; font-size: 19px; line-height: 26px; color: var(--paper);
  }
  .subtitle strong { font-weight: 600; color: var(--pale-blush); display: block; margin-bottom: 6px; }
  .author {
    position: absolute; left: 36px; bottom: 46px;
    font-weight: 600; font-size: 46px; letter-spacing: 3px; color: var(--paper); line-height: 1;
  }
</style>
</head>
<body>
  <div class="cover-wrap">

    <section class="back-cover">
      <p class="back-tagline">A brutally honest recovery story—about what happens after you get clean, and the ego you still have to face.</p>
      <div class="back-rule"></div>
      <p class="back-hook">Most people think addiction ends when you put down the drink, the drug, or the chaos.</p>
      <div class="back-blurb">
        <p>But for Marek Tollan, sobriety was just the start. Behind the personal development posts, six-pack selfies, and billion-rand property deals, he was still chasing the one thing rehab never took from him: the need to be admired.</p>
        <p>This book is not a confession. It’s a dismantling.</p>
        <p>In The Quiet Lantern Keeper, Marek exposes the hidden patterns of ego, control, and validation-seeking that nearly cost him everything—even after he got “better.” With fearless self-inquiry and raw storytelling, he invites readers into his recovery from performance, perfectionism, and power addiction.</p>
        <p>Whether you’ve been the narcissist—or you’ve loved one—this book is a mirror. And what you’ll find is not just insight, but a new path forward: one where truth is more powerful than charm, and safety matters more than being impressive.</p>
      </div>
      <p class="back-closing">This isn’t about being perfect.<br>It’s about being honest.<br>And finally becoming someone worth trusting—especially by yourself.</p>
    </section>

    <section class="spine">
      <span class="spine-title">THE QUIET <b>LANTERN KEEPER</b></span>
      <span class="spine-author">MAREK TOLLAN</span>
    </section>

    <section class="front-cover">
      <svg class="portrait" viewBox="0 0 275 748" preserveAspectRatio="none" role="img" aria-label="Author portrait split down the middle: the raw, heavy self on the left half in sepia and the calm, lighter self on the right half in cool grey">
        <defs>
          <linearGradient id="sepiaHalf" x1="0" y1="0" x2="1" y2="0">
            <stop offset="0" stop-color="#1f1c1d"/>
            <stop offset="0.45" stop-color="#3a2e2a"/>
            <stop offset="1" stop-color="#5c4a42"/>
          </linearGradient>
          <linearGradient id="slateHalf" x1="0" y1="0" x2="0" y2="1">
            <stop offset="0" stop-color="#2e353c"/>
            <stop offset="0.5" stop-color="#4d5862"/>
            <stop offset="1" stop-color="#2e353c"/>
          </linearGradient>
        </defs>
        <rect x="0" y="0" width="138" height="748" fill="url(#sepiaHalf)"/>
        <rect x="138" y="0" width="137" height="748" fill="url(#slateHalf)"/>
        <rect x="137" y="0" width="2" height="748" fill="#eb3d1f"/>
      </svg>

      <p class="endorsement">“Whatever we’ve been through, Marek not only makes us feel we can get over it, he gives us the tools to do exactly that.” <span class="credit">— ALDO FENNICK</span></p>

      <div class="title-block">
        <div class="title-lead">THE</div>
        <div class="title-main">Quiet</div>
        <div class="title-main">Lantern</div>
        <div class="title-main">Keeper</div>
        <div class="title-rule"></div>
      </div>

      <p class="subtitle"><strong>Not every narcissist is a monster.</strong>Some are just wounded men trying their best to survive</p>

      <div class="author">MAREK TOLLAN</div>
    </section>

  </div>
</body>
</html>
```